BVH Business Card Design

We are a small construction equipment rental and hardware store located in Middle Tennessee. We have three stores. Our primary business is construction equipment. We have an existing logo we'd like to use. I think I would like to list each store physical address on the back of the card and maybe the web address also: www.bvhhireyard.example.

We also need a design that we can incorporate into company letterhead, small note pads, and even checks if possible.

Industry/Entity Type

Construction

Contact Information for Business Card

We have our Logo, Name: Brookvale Hauling Machinery, Employee Name, Main Phone Number, Mobile Phone Number, Email Address, Company Address, and website information (There are three locations that can go on the back if necessary) We would like to leave some room on the back of the card in case we want to write information down on it.

```html
<!DOCTYPE html>
<html lang="en">
<head>
<meta charset="utf-8">
<title>BVH Business Card</title>
<link href="https://fonts.googleapis.com/css2?family=Montserrat:wght@700&family=Open+Sans:wght@400;600&display=swap" rel="stylesheet">
<style>
  :root {
    --navy: #22306a;
    --red: #e8283a;
    --slate: #545b6b;
    --ink: #1d1f2a;
    --rule: #9a9ca4;
    --paper: #ffffff;
    --stage: #5c5c5c;
  }
  html, body { margin: 0; padding: 0; overflow: hidden; }
  body {
    width: 1200px; height: 820px; position: relative;
    background: var(--stage);
    font-family: "Open Sans", Arial, sans-serif;
  }
  .card {
    position: absolute; top: 258px; width: 471px; height: 271px;
    border-radius: 16px; overflow: hidden;
  }
  .card--front { left: 117px; background: var(--paper); }
  .card--back { left: 628px; background: var(--navy); }

  .mark {
    position: absolute; width: 54px; height: 54px; border-radius: 50%;
    background: var(--red); color: #fff;
    font-family: "Montserrat", Arial, sans-serif; font-weight: 700; font-size: 15px;
    display: flex; align-items: center; justify-content: center;
  }
  .company {
    position: absolute; margin: 0;
    font-family: "Montserrat", Arial, sans-serif; font-weight: 700;
    font-size: 19px; line-height: 23px; text-align: center;
  }
  .card--front .mark { left: 23px; top: 34px; }
  .card--front .company { left: 82px; top: 41px; color: var(--slate); }
  .card--back .mark { left: 65px; top: 40px; }
  .card--back .company { left: 124px; top: 46px; color: #fff; }

  .person { position: absolute; right: 28px; top: 111px; text-align: right; }
  .person__name { font-size: 19px; color: var(--ink); line-height: 24px; }
  .person__title { font-size: 13px; color: var(--navy); line-height: 18px; }
  .rule { position: absolute; top: 150px; height: 2px; }
  .rule--grey { left: 23px; width: 283px; background: var(--rule); }
  .rule--red { left: 310px; width: 134px; background: var(--red); }

  .contacts { position: absolute; left: 22px; top: 162px; margin: 0; padding: 0; list-style: none; }
  .contacts li {
    font-size: 12px; color: var(--ink); height: 19px;
    display: flex; align-items: center; gap: 7px;
  }
  .contacts svg { width: 10px; height: 10px; fill: var(--navy); }
  .address-front {
    position: absolute; right: 27px; top: 163px; margin: 0;
    font-size: 11.5px; line-height: 19px; text-align: right; color: var(--ink); font-style: normal;
  }

  .band { position: absolute; left: 0; bottom: 0; width: 100%; height: 26px; }
  .band__navy { position: absolute; left: 0; top: 0; width: 310px; height: 100%; background: var(--navy); }
  .band__red { position: absolute; left: 310px; top: 0; right: 0; height: 100%; background: var(--red); }
  .band__dot {
    position: absolute; left: 305px; top: 0; width: 26px; height: 26px; border-radius: 50%;
    background: var(--paper); box-sizing: border-box; border: 3px solid var(--red);
  }

  .locations { position: absolute; left: 126px; top: 118px; margin: 0; }
  .locations div { display: flex; height: 25.5px; font-size: 12px; line-height: 18px; }
  .locations dt { color: var(--red); width: 62px; }
  .locations dd { margin: 0; color: #fff; }
  .site {
    position: absolute; left: 0; right: 0; top: 198px;
    display: flex; align-items: center; justify-content: center; gap: 6px;
    color: #fff; font-size: 13px;
  }
  .site__line { width: 50px; height: 1.5px; background: #fff; }
  .site em { font-style: normal; color: var(--red); }
</style>
</head>
<body>
  <section class="card card--front">
    <div class="mark">BVH</div>
    <h1 class="company">BROOKVALE HAULING<br>MACHINERY</h1>
    <div class="person">
      <div class="person__name">Your Name</div>
      <div class="person__title">Job title</div>
    </div>
    <div class="rule rule--grey"></div>
    <div class="rule rule--red"></div>
    <ul class="contacts">
      <li><svg viewBox="0 0 10 10"><path d="M2 0l2 2.5-1 1.2c.6 1.4 1.6 2.4 3 3l1.2-1L10 8l-1.2 1.6C4.5 9.4.6 5.5.4 1.2z"/></svg>615-555-0142</li>
      <li><svg viewBox="0 0 10 10"><rect x="0" y="3" width="4" height="7"/><rect x="5" y="1" width="5" height="9"/></svg>615-555-0148</li>
      <li><svg viewBox="0 0 10 10"><path d="M0 2h10v6H0z M0 2l5 3.5L10 2" stroke="#fff" stroke-width=".8"/></svg>jmorrow@bvhhireyard.example</li>
      <li><svg viewBox="0 0 10 10"><circle cx="5" cy="5" r="4.5"/><path d="M.5 5h9M5 .5v9" stroke="#fff" stroke-width=".7"/></svg>www.bvhhireyard.example</li>
    </ul>
    <address class="address-front">1820 Millbrook Rd Brookvale,<br>TN 37100.</address>
    <div class="band">
      <div class="band__navy"></div>
      <div class="band__red"></div>
      <div class="band__dot"></div>
    </div>
  </section>

  <section class="card card--back">
    <div class="mark">BVH</div>
    <h2 class="company">BROOKVALE HAULING<br>MACHINERY</h2>
    <dl class="locations">
      <div><dt>Adress 1</dt><dd>1820 Millbrook Rd Brookvale, 1233</dd></div>
      <div><dt>Adress 2</dt><dd>1820 Millbrook Rd Brookvale, 33</dd></div>
      <div><dt>Adress 3</dt><dd>1820 Millbrook Rd Brookvale, 233</dd></div>
    </dl>
    <div class="site"><span class="site__line"></span><span>www.<em>bvhhireyard</em>.example</span><span class="site__line"></span></div>
  </section>
</body>
</html>
```